Catchy Cards for Hospital

I run a rural hospital in Texas called Pellor Valley Hospital and am in need of contemporary business cards for all of my Department Heads. While our logo is somewhat simplistic, I don't have the option of changing it at this time, so anything to make the rest of the card present the appearance of a modern, professional healthcare facility would be great. Although the attached files are in black, our hospital colors are in a copper brown and black. I need to be able to change the name and title on the card so I can get cards printed for various department heads.

Target Market(s)

Referring physicians, large hospital systems, national organizations, state and federal government

Industry/Entity Type

Hospital

Contact Information for Business Card

Name Dale Hoskin
Title CEO

Phone: Main 555-555-0147 & Direct xxxxxx
Fax xxxxx
dale.hoskin@pellorvh.example
382 Wimble Street Box 415
Harlow, Westvale 76902

Font styles to use
Serif

Colors
f48340

Requirements
Must have
• Clean crisp lines and ability to modify names, titles and emails
• On the back "PellorValleyHospital.Example
Nice to have
• Needs to be in line with logo, which is a bit dated and not too appealing, but I'm hoping that the rest of the card can make up for that fact just a little bit.
• Hospital's colors are a copper brown, black and white
Should not have
• Shapes or anything distracting

```html
<!DOCTYPE html>
<html lang="en">
<head>
<meta charset="utf-8">
<title>Pellor Valley Hospital – Business Card</title>
<link rel="stylesheet" href="https://fonts.googleapis.com/css2?family=Mulish:wght@300;400;700&display=swap">
<style>
  :root {
    --copper: #f26a2e;
    --ink: #0a0a0a;
    --paper: #ffffff;
  }
  * { margin: 0; padding: 0; box-sizing: border-box; }
  html, body { width: 1200px; height: 734px; overflow: hidden; background: var(--paper); }
  .card {
    position: relative;
    width: 1200px;
    height: 734px;
    background: var(--paper);
    font-family: "Mulish", "Century Gothic", sans-serif;
    color: var(--ink);
  }
  .brand-name {
    position: absolute;
    left: 716px;
    top: 70px;
    width: 420px;
    color: var(--copper);
    font-weight: 700;
    font-size: 58px;
    line-height: 1.12;
  }
  .person-name {
    position: absolute;
    left: 72px;
    top: 298px;
    font-size: 39px;
    font-weight: 700;
    line-height: 1;
  }
  .person-title {
    position: absolute;
    left: 72px;
    top: 346px;
    font-size: 32px;
    font-weight: 300;
    line-height: 1;
  }
  .divider {
    position: absolute;
    left: 71px;
    top: 386px;
    width: 1058px;
    height: 5px;
    background: var(--ink);
  }
  .org-name {
    position: absolute;
    left: 72px;
    top: 440px;
    font-size: 39px;
    font-weight: 700;
    line-height: 1;
  }
  .contact {
    position: absolute;
    left: 72px;
    top: 494px;
    font-size: 26px;
    font-weight: 400;
    line-height: 28.5px;
  }
  .contact .indent { padding-left: 101px; }
  .address {
    position: absolute;
    left: 803px;
    top: 536px;
    font-size: 26px;
    font-weight: 400;
    line-height: 29px;
  }
  .footer-bands {
    position: absolute;
    left: 0;
    top: 0;
    width: 1200px;
    height: 734px;
  }
  .band-copper { fill: var(--copper); }
  .band-ink { fill: var(--ink); }
</style>
</head>
<body>
  <div class="card">
    <div class="brand-name">Pellor Valley Hospital</div>

    <div class="person-name">Dale Hoskin</div>
    <div class="person-title">CEO</div>
    <div class="divider"></div>

    <div class="org-name">Pellor Valley Hospital</div>
    <div class="contact">
      <div>Phone: Main 555-555-0147</div>
      <div class="indent">Direct</div>
      <div>Fax:</div>
      <div>dale.hoskin@pellorvh.example</div>
    </div>

    <div class="address">
      <div>382 Wimble Street Box 415</div>
      <div>Harlow, Westvale 76902</div>
    </div>

    <svg class="footer-bands" viewBox="0 0 1200 734" aria-hidden="true">
      <polygon class="band-copper" points="0,688 441,688 472,711 1200,711 1200,734 0,734"/>
      <polygon class="band-ink" points="458,688 1200,688 1200,702 476,702"/>
    </svg>
  </div>
</body>
</html>
```